Vehicle Rental Hire in the Algarve - Portugal

We are opening a Vehicle Rental company in the Algarve - Portugal - this will attract both locals and Tourists visiting. So we want this website to capture the beautiful location we will be set in, along with the familiarity of a vehicle rental company. And to keep a colour scheme in Line with out Logo. We are Marlenic Vehicle Rental.

Industry/Entity Type

Vehicle Rental

Number of Pages Required

1 page

Requirements
Must have
• must be professional, and simple to use navigation bar - must also have a "make a reservation" box - similar to the screenshot attached - Under our logo it must read "Vehicle Rental"
Nice to have
• It needs to be in a colour scheme that fits in with our logo

```html
<!DOCTYPE html>
<html lang="en">
<head>
<meta charset="utf-8">
<title>Marlenic Vehicle Rental</title>
<link href="https://fonts.googleapis.com/css2?family=Barlow+Condensed:wght@600;700&family=Montserrat:wght@400;500;600;700&display=swap" rel="stylesheet">
<style>
:root{
  --red:#c0342d;
  --red-soft:#d1574f;
  --red-deep:#a82a24;
  --blue:#2a1ee0;
  --lavender:#a9a3f5;
  --ink:#1f1f1f;
  --muted:#6b6b6b;
  --line:#e6e6e6;
  --footer:#252423;
  --white:#ffffff;
}
*{box-sizing:border-box;margin:0;padding:0}
html,body{width:1200px;height:4693px;overflow:hidden}
body{position:relative;background:var(--white);font-family:"Montserrat",sans-serif;color:var(--ink)}
.abs{position:absolute}
.heading{font-family:"Barlow Condensed",sans-serif;font-weight:700;text-transform:uppercase;letter-spacing:-.2px}
.lead{font-size:11.5px;line-height:19px;color:#333;text-align:center}

/* nav */
.site-nav{top:0;left:0;width:1200px;height:55px;background:var(--white);z-index:5}
.nav-links{top:21px;display:flex;gap:0;font-size:10.5px;color:#444}
.nav-links span{margin-right:38px}
.nav-left{left:124px}
.nav-right{left:736px}
.brand-badge{left:536px;top:-8px;width:128px;height:128px;border-radius:50%;background:var(--white);z-index:6;text-align:center;padding-top:44px;box-shadow:0 3px 8px rgba(0,0,0,.08)}
.brand-name{font-family:"Barlow Condensed",sans-serif;font-weight:700;font-size:25px;color:var(--blue);letter-spacing:.5px}
.brand-tag{font-size:9px;color:var(--red);font-weight:500;margin-top:1px}

/* hero */
.hero{top:55px;left:0;width:1200px;height:630px;overflow:hidden}
.hero-photo{right:0;top:0;width:700px;height:630px;background:linear-gradient(135deg,#6d3a2a 0%,#a8613c 35%,#d9a27c 60%,#4a3a36 100%)}
.hero-red{left:0;top:0;width:720px;height:630px;background:linear-gradient(90deg,var(--red) 0%,var(--red) 62%,rgba(192,52,45,.55) 85%,rgba(192,52,45,0) 100%)}
.partner-login{left:124px;top:16px;color:var(--white);font-size:10px;display:flex;align-items:center;gap:8px}
.partner-rule{left:124px;top:34px;width:380px;height:1px;background:rgba(255,255,255,.5)}
.lang{left:1000px;top:14px;color:var(--white);font-size:10px;display:flex;align-items:center;gap:6px}
.hero-title{left:124px;top:118px;color:var(--white);font-size:42px;line-height:42px;width:440px}
.hero-text{left:124px;top:263px;width:400px;color:var(--white);font-size:11px;line-height:19px}
.btn-outline{border:2px solid var(--white);color:var(--white);border-radius:20px;font-size:10px;font-weight:700;display:flex;align-items:center;justify-content:center;letter-spacing:.3px}
.hero-btn{left:124px;top:366px;width:171px;height:38px}
.dot{position:absolute;width:7px;height:7px;border-radius:50%;background:var(--blue);right:-2px;bottom:-3px}

/* reservation */
.reservation{left:124px;top:539px;width:870px;height:397px;background:var(--white);border-left:5px solid var(--blue);box-shadow:0 4px 18px rgba(0,0,0,.14);z-index:3}
.res-title{left:64px;top:50px;font-family:"Barlow Condensed",sans-serif;font-weight:600;font-size:28px;text-transform:uppercase;color:var(--ink)}
.res-rule{left:64px;top:88px;width:740px;height:1px;background:var(--line)}
.field-label{font-size:9.5px;color:#333}
.field{height:40px;background:var(--white);box-shadow:0 2px 8px rgba(0,0,0,.12);font-size:9.5px;color:#444;display:flex;align-items:center;justify-content:space-between;padding:0 18px}
.caret{width:0;height:0;border-left:4px solid transparent;border-right:4px solid transparent;border-top:5px solid #333}
.search-btn{left:428px;top:304px;width:335px;height:40px;background:var(--red);border-radius:20px;color:var(--white);font-size:10px;font-weight:700;display:flex;align-items:center;justify-content:center}

/* how it works */
.how-title{left:0;top:1028px;width:1200px;text-align:center;font-size:34px}
.how-text{left:182px;top:1090px;width:836px}
.step-label{top:1376px;width:120px;text-align:center;font-family:"Barlow Condensed",sans-serif;font-weight:600;font-size:14px;line-height:20px;text-transform:uppercase}

/* services */
.services{top:1511px;left:0;width:1200px;height:632px}
.services-photo{left:0;top:0;width:600px;height:632px;background:linear-gradient(160deg,#d8d2c6 0%,#b4ab9c 45%,#3a3d52 75%,#27293a 100%)}
.services-panel{left:600px;top:0;width:600px;height:632px;background:var(--red)}
.services-title{left:63px;top:50px;color:var(--white);font-size:35px;line-height:37px}
.services-text{left:63px;top:182px;width:360px;color:var(--white);font-size:11px;line-height:19px}
.perk{left:63px;width:390px;height:93px;background:var(--red-soft);padding:20px 32px;color:var(--white)}
.perk h4{font-family:"Barlow Condensed",sans-serif;font-weight:700;font-size:15px;text-transform:uppercase;margin-bottom:6px}
.perk p{font-size:9px;line-height:16px;width:300px}
.perk-icon{position:absolute;right:-24px;top:24px;width:44px;height:44px;border-radius:50%;background:var(--white);display:flex;align-items:center;justify-content:center}

/* fleet */
.fleet-title{left:0;top:2234px;width:1200px;text-align:center;font-size:34px}
.fleet-text{left:251px;top:2297px;width:698px}
.car-card{top:2400px;width:302px;height:377px;background:var(--white);box-shadow:0 4px 16px rgba(0,0,0,.1);border-radius:6px;text-align:center}
.car-photo{position:absolute;left:0;top:-10px;width:302px;height:120px;border-radius:8px;background:linear-gradient(180deg,#f1f1f1 0%,#c9c9c9 55%,#8a8a8a 100%)}
.car-name{position:absolute;left:0;top:152px;width:302px;font-family:"Barlow Condensed",sans-serif;font-weight:600;font-size:16px;text-transform:uppercase}
.car-specs{position:absolute;left:40px;top:182px;width:222px;display:flex;justify-content:space-between;font-size:8.5px;color:#777}
.car-specs div{display:flex;flex-direction:column;align-items:center;gap:3px;width:60px}
.car-from{position:absolute;left:0;top:236px;width:302px;font-size:7px;font-weight:700;color:#333}
.car-price{position:absolute;left:0;top:250px;width:302px;font-family:"Barlow Condensed",sans-serif;font-weight:700;font-size:20px;color:var(--red)}
.car-btn{position:absolute;top:300px;height:36px;border-radius:18px;font-size:9.5px;font-weight:700;display:flex;align-items:center;justify-content:center}
.car-btn.details{left:20px;width:126px;background:var(--red);color:var(--white)}
.car-btn.book{left:160px;width:122px;border:2px solid var(--red);color:var(--ink)}
.car-btn .dot{right:4px;bottom:-2px}
.view-all{left:432px;top:2819px;width:336px;height:40px;border-radius:20px;background:var(--blue);color:var(--white);font-size:10px;font-weight:700;display:flex;align-items:center;justify-content:center}
.view-all .dot{background:var(--red);right:6px;bottom:-3px}

/* passport */
.passport{top:2959px;left:0;width:1200px;height:732px;overflow:hidden}
.passport-photo{left:0;top:0;width:1200px;height:732px;background:linear-gradient(180deg,#c7cbd3 0%,#a29a8e 30%,#6f6457 60%,#4c4540 100%)}
.passport-band{left:0;top:461px;width:1200px;height:230px;background:rgba(192,52,45,.85)}
.passport-title{left:124px;top:506px;color:var(--white);font-size:36px;line-height:40px}
.passport-text{left:124px;top:611px;width:560px;color:var(--white);font-size:10px;line-height:18px}
.passport-btn{left:903px;top:554px;width:171px;height:38px}

/* testimonials */
.reviews-title{left:0;top:3786px;width:1200px;text-align:center;font-size:34px}
.reviews-text{left:262px;top:3843px;width:676px}
.review{top:3928px;width:464px;height:187px;background:var(--white);box-shadow:0 4px 16px rgba(0,0,0,.1)}
.review-photo{position:absolute;left:18px;top:17px;width:162px;height:158px}
.review-name{position:absolute;left:202px;top:44px;font-family:"Barlow Condensed",sans-serif;font-weight:700;font-size:15px;text-transform:uppercase}
.review-text{position:absolute;left:202px;top:72px;width:240px;font-size:9.5px;line-height:18px;color:#333}
.quote{position:absolute;right:20px;bottom:16px;font-family:"Barlow Condensed",sans-serif;font-weight:700;font-size:42px;line-height:30px;color:var(--blue)}
.slider-arrow{top:4007px;width:30px;height:32px;background:var(--red);display:flex;align-items:center;justify-content:center}

/* footer */
.site-footer{top:4219px;left:0;width:1200px;height:474px;background:var(--footer);color:var(--white)}
.footer-brand{left:124px;top:100px;width:170px;height:100px;text-align:center}
.footer-brand .brand-name{color:var(--white);font-size:28px;margin-top:28px}
.footer-brand .brand-tag{color:#e06b63}
.footer-ring{left:158px;top:88px;width:120px;height:120px;border-radius:50%;border:1.5px solid rgba(255,255,255,.75)}
.footer-about{left:124px;top:237px;width:230px;font-size:10px;line-height:23px;color:#e8e8e8}
.social{top:364px;width:26px;height:26px;border-radius:50%;background:var(--red)}
.footer-heading{font-family:"Barlow Condensed",sans-serif;font-weight:700;font-size:16px;text-transform:uppercase}
.footer-links{left:393px;top:180px;font-size:10px;line-height:23.6px;color:#e8e8e8}
.contact-item{left:608px;display:flex;align-items:flex-start;gap:14px;font-size:10px;line-height:18px;color:#e8e8e8}
.contact-icon{width:24px;height:24px;border-radius:50%;background:var(--red);display:flex;align-items:center;justify-content:center;flex:none}
.news-input{left:810px;top:246px;width:184px;height:33px;background:var(--white);font-size:8.5px;color:#888;padding:0 16px;display:flex;align-items:center}
.news-submit{left:994px;top:246px;width:80px;height:33px;background:var(--red);font-size:8.5px;font-weight:700;display:flex;align-items:center;justify-content:center}
</style>
</head>
<body>

<!-- navigation -->
<header class="site-nav abs">
  <nav class="nav-links nav-left abs"><span>Home</span><span>About Us</span><span>Promotions</span><span>Extras &amp; Services</span></nav>
  <nav class="nav-links nav-right abs"><span style="margin-right:48px">Fleet</span><span style="margin-right:48px">Partners</span><span style="margin-right:48px">Contacts</span><span style="margin-right:0">Rates &amp; Reservations</span></nav>
</header>
<div class="brand-badge abs">
  <div class="brand-name">MARLENIC</div>
  <div class="brand-tag">Vehicle Rental</div>
</div>

<!-- hero -->
<section class="hero abs">
  <div class="hero-photo abs" role="img" aria-label="Smiling couple pouring a drink beside the open boot of a rental car"></div>
  <div class="hero-red abs"></div>
  <div class="partner-login abs">
    <svg width="11" height="11" viewBox="0 0 12 12"><circle cx="6" cy="3.5" r="2.6" fill="#fff"/><path d="M1 12c0-3 2.2-5 5-5s5 2 5 5z" fill="#fff"/></svg>
    Partner Login
  </div>
  <div class="partner-rule abs"></div>
  <div class="lang abs">
    <svg width="12" height="12" viewBox="0 0 12 12"><circle cx="6" cy="6" r="5.2" fill="none" stroke="#fff" stroke-width="1.2"/><path d="M1 6h10M6 1c2 2 2 8 0 10M6 1c-2 2-2 8 0 10" fill="none" stroke="#fff" stroke-width=".9"/></svg>
    English <span style="font-size:7px">▼</span>
  </div>
  <h1 class="hero-title heading abs">Renting made simple, memories made forever</h1>
  <p class="hero-text abs">Lorem Ipsum is simply dummy text of the printing and typesetting industry. Lorem Ipsum has been the industry's standard dummy text ever since the 1500s, when an unknown printer took a galley of type and scrambled it to make a type specimen book.</p>
  <div class="hero-btn btn-outline abs">RENT A CAR<span class="dot"></span></div>
</section>

<!-- reservation -->
<section class="reservation abs">
  <h2 class="res-title abs">Make a Reservation</h2>
  <div class="res-rule abs"></div>

  <div class="field-label abs" style="left:64px;top:126px">Pick Up Location</div>
  <div class="field abs" style="left:64px;top:138px;width:337px">Please Choose... <span class="caret"></span></div>
  <div class="field-label abs" style="left:423px;top:126px">Driver's Age</div>
  <div class="field abs" style="left:423px;top:138px;width:337px">Please Choose... <span class="caret"></span></div>

  <div class="field-label abs" style="left:64px;top:209px">Vehicle category</div>
  <div class="field abs" style="left:64px;top:222px;width:337px">Please Choose... <span class="caret"></span></div>
  <div class="field-label abs" style="left:423px;top:209px">Pick Up Date</div>
  <div class="field abs" style="left:423px;top:222px;width:142px">dd-mm-aaaa</div>
  <div class="field-label abs" style="left:585px;top:209px">Hour</div>
  <div class="field abs" style="left:585px;top:222px;width:140px">9:00 <span class="caret"></span></div>

  <div class="field-label abs" style="left:64px;top:291px">Drop Off Date</div>
  <div class="field abs" style="left:64px;top:304px;width:142px">dd-mm-aaaa</div>
  <div class="field-label abs" style="left:228px;top:291px">Hour</div>
  <div class="field abs" style="left:228px;top:304px;width:140px">9:00 <span class="caret"></span></div>
  <div class="search-btn abs">SEARCH<span class="dot"></span></div>
</section>

<!-- how it works -->
<h2 class="how-title heading abs">How It Works</h2>
<p class="how-text lead abs">Lorem Ipsum is simply dummy text of the printing and typesetting industry. Lorem Ipsum has been the industry's standard dummy text ever since the 1500s, when an unknown printer took a galley of type and scrambled it to make a type specimen book.</p>
<svg class="abs" style="left:0;top:1160px" width="1200" height="220" viewBox="0 1160 1200 220" aria-hidden="true">
  <g fill="none" stroke="var(--red)" stroke-width="1.6">
    <path d="M327 1272 A91 91 0 0 1 508 1262"/>
    <path d="M509 1266 A91 91 0 0 0 690 1272"/>
    <path d="M691 1262 A91 91 0 0 1 872 1270"/>
  </g>
  <g fill="var(--red)">
    <path d="M504 1262 l8 0 l-4 9z"/>
    <path d="M686 1272 l8 0 l-4 -9z"/>
    <path d="M868 1269 l8 0 l-4 9z"/>
  </g>
  <g>
    <circle cx="417" cy="1269" r="71" fill="var(--lavender)"/><circle cx="417" cy="1269" r="48" fill="var(--blue)"/>
    <circle cx="599" cy="1269" r="71" fill="var(--lavender)"/><circle cx="599" cy="1269" r="48" fill="var(--blue)"/>
    <circle cx="781" cy="1269" r="71" fill="var(--lavender)"/><circle cx="781" cy="1269" r="48" fill="var(--blue)"/>
  </g>
  <g fill="none" stroke="#fff" stroke-width="2" stroke-linecap="round" stroke-linejoin="round">
    <circle cx="417" cy="1260" r="8"/><circle cx="417" cy="1260" r="3"/>
    <path d="M417 1268 v8 M401 1282 h32 l-4 -8 h-24z"/>
    <rect x="583" y="1255" width="32" height="28" rx="3"/><path d="M583 1263 h32 M591 1251 v7 M607 1251 v7 M590 1270 h4 M598 1270 h4 M606 1270 h4 M590 1277 h4 M598 1277 h4"/>
    <path d="M768 1270 l9 9 l18 -20"/>
  </g>
</svg>
<div class="step-label abs" style="left:357px">Choose<br>Location</div>
<div class="step-label abs" style="left:539px">Pick-up<br>Date</div>
<div class="step-label abs" style="left:721px">Book<br>Your Car</div>

<!-- services -->
<section class="services abs">
  <div class="services-photo abs" role="img" aria-label="Hand in a suit sleeve holding out a car key"></div>
  <div class="services-panel abs">
    <h2 class="services-title heading abs">Feel the best services with our rental deals</h2>
    <p class="services-text abs">Lorem Ipsum is simply dummy text of the printing and typesetting industry.</p>
    <div class="perk abs" style="top:254px"><h4>Deal for every budget</h4><p>Lorem Ipsum is simply dummy text of the printing and typesetting industry.</p>
      <span class="perk-icon"><svg width="24" height="24" viewBox="0 0 24 24" fill="none" stroke="var(--red)" stroke-width="1.6"><circle cx="12" cy="12" r="9"/><path d="M14.5 9c-.5-1-1.5-1.5-2.5-1.5-1.5 0-2.5.8-2.5 2s1 1.7 2.5 2 2.5.8 2.5 2-1 2-2.5 2c-1 0-2-.5-2.5-1.5M12 6v1.5M12 16.5V18"/></svg></span></div>
    <div class="perk abs" style="top:366px"><h4>Best price guaranteed</h4><p>Lorem Ipsum is simply dummy text of the printing and typesetting industry.</p>
      <span class="perk-icon"><svg width="24" height="24" viewBox="0 0 24 24" fill="none" stroke="var(--red)" stroke-width="1.6"><path d="M4 12l8-8h6v6l-8 8z"/><circle cx="15" cy="7" r="1.3"/></svg></span></div>
    <div class="perk abs" style="top:479px"><h4>Support 24/7</h4><p>Lorem Ipsum is simply dummy text of the printing and typesetting industry.</p>
      <span class="perk-icon"><svg width="24" height="24" viewBox="0 0 24 24" fill="none" stroke="var(--red)" stroke-width="1.6"><path d="M7 4h4l1 4-2 1.5a10 10 0 0 0 4.5 4.5L16 12l4 1v4a2 2 0 0 1-2 2A15 15 0 0 1 5 6a2 2 0 0 1 2-2z"/></svg></span></div>
  </div>
</section>

<!-- fleet -->
<h2 class="fleet-title heading abs">Top Rated Rented Cars</h2>
<p class="fleet-text lead abs">Lorem Ipsum is simply dummy text of the printing and typesetting industry. Lorem Ipsum has been the industry's standard dummy text ever since the 1500s, when an unknown printer took a galley of type and scrambled it to make a type specimen book.</p>

<article class="car-card abs" style="left:124px">
  <div class="car-photo" role="img" aria-label="Silver compact sedan, side view"></div>
  <div class="car-name">Coastline Compact</div>
  <div class="car-specs"><div><svg width="12" height="12" viewBox="0 0 12 12" fill="none" stroke="var(--red)"><circle cx="6" cy="3.5" r="2.3"/><path d="M1.5 11.5c0-2.7 2-4.5 4.5-4.5s4.5 1.8 4.5 4.5z"/></svg>4 Seater</div><div><svg width="12" height="12" viewBox="0 0 12 12" fill="none" stroke="var(--red)"><circle cx="6" cy="6" r="5"/><circle cx="6" cy="6" r="1.5"/></svg>Manual</div><div><svg width="12" height="12" viewBox="0 0 12 12" fill="none" stroke="var(--red)"><circle cx="6" cy="6" r="5"/><path d="M6 6l2.5-2.5"/></svg>5Km/1-lt</div></div>
  <div class="car-from">STARTING AT</div>
  <div class="car-price">$300/DAY</div>
  <div class="car-btn details">DETAILS<span class="dot"></span></div>
  <div class="car-btn book">BOOK NOW<span class="dot"></span></div>
</article>
<article class="car-card abs" style="left:448px">
  <div class="car-photo" role="img" aria-label="Black sport hatchback, side view"></div>
  <div class="car-name">Ria Sport Hatch</div>
  <div class="car-specs"><div><svg width="12" height="12" viewBox="0 0 12 12" fill="none" stroke="var(--red)"><circle cx="6" cy="3.5" r="2.3"/><path d="M1.5 11.5c0-2.7 2-4.5 4.5-4.5s4.5 1.8 4.5 4.5z"/></svg>4 Seater</div><div><svg width="12" height="12" viewBox="0 0 12 12" fill="none" stroke="var(--red)"><circle cx="6" cy="6" r="5"/><circle cx="6" cy="6" r="1.5"/></svg>Manual</div><div><svg width="12" height="12" viewBox="0 0 12 12" fill="none" stroke="var(--red)"><circle cx="6" cy="6" r="5"/><path d="M6 6l2.5-2.5"/></svg>5Km/1-lt</div></div>
  <div class="car-from">STARTING AT</div>
  <div class="car-price">$350/DAY</div>
  <div class="car-btn details">DETAILS<span class="dot"></span></div>
  <div class="car-btn book">BOOK NOW<span class="dot"></span></div>
</article>
<article class="car-card abs" style="left:772px">
  <div class="car-photo" role="img" aria-label="Silver compact SUV, side view"></div>
  <div class="car-name">Serra SUV</div>
  <div class="car-specs"><div><svg width="12" height="12" viewBox="0 0 12 12" fill="none" stroke="var(--red)"><circle cx="6" cy="3.5" r="2.3"/><path d="M1.5 11.5c0-2.7 2-4.5 4.5-4.5s4.5 1.8 4.5 4.5z"/></svg>6 Seater</div><div><svg width="12" height="12" viewBox="0 0 12 12" fill="none" stroke="var(--red)"><circle cx="6" cy="6" r="5"/><circle cx="6" cy="6" r="1.5"/></svg>Manual</div><div><svg width="12" height="12" viewBox="0 0 12 12" fill="none" stroke="var(--red)"><circle cx="6" cy="6" r="5"/><path d="M6 6l2.5-2.5"/></svg>5Km/1-lt</div></div>
  <div class="car-from">STARTING AT</div>
  <div class="car-price">$250/DAY</div>
  <div class="car-btn details">DETAILS<span class="dot"></span></div>
  <div class="car-btn book">BOOK NOW<span class="dot"></span></div>
</article>
<div class="view-all abs">VIEW ALL CARS<span class="dot"></span></div>

<!-- passport -->
<section class="passport abs">
  <div class="passport-photo abs" role="img" aria-label="Four friends with ice cream cones and cameras on a sunny town street"></div>
  <div class="passport-band abs"></div>
  <h2 class="passport-title heading abs">Your passport to freedom:<br>rent, explore, enjoy</h2>
  <p class="passport-text abs">Lorem Ipsum is simply dummy text of the printing and typesetting industry. Lorem Ipsum has been the industry's standard dummy text ever since the 1500s.</p>
  <div class="passport-btn btn-outline abs">RENT A CAR<span class="dot"></span></div>
</section>

<!-- testimonials -->
<h2 class="reviews-title heading abs">What Our Customers Says!</h2>
<p class="reviews-text lead abs">Lorem Ipsum is simply dummy text of the printing and typesetting industry. Lorem Ipsum has been the industry's standard dummy text ever since the 1500s.</p>
<div class="slider-arrow abs" style="left:91px;border-radius:16px 0 0 16px"><svg width="12" height="10" viewBox="0 0 12 10" fill="none" stroke="#fff" stroke-width="1.4"><path d="M11 5H1M5 1L1 5l4 4"/></svg></div>
<div class="slider-arrow abs" style="left:1080px;border-radius:0 16px 16px 0"><svg width="12" height="10" viewBox="0 0 12 10" fill="none" stroke="#fff" stroke-width="1.4"><path d="M1 5h10M7 1l4 4-4 4"/></svg></div>
<article class="review abs" style="left:124px">
  <div class="review-photo" style="background:linear-gradient(150deg,#d9cfc1,#9c8a74 60%,#c56b5d)" role="img" aria-label="Couple holding a rental booking outside a shop"></div>
  <div class="review-name">Tomas &amp; Alina</div>
  <p class="review-text">Lorem Ipsum is simply dummy text of the printing and typesetting industry. Lorem Ipsum has been the industry's standard dummy text ever since the 1500s.</p>
  <div class="quote">”</div>
</article>
<article class="review abs" style="left:610px">
  <div class="review-photo" style="background:linear-gradient(150deg,#e4e4e4,#8f8f92 55%,#4b4d57)" role="img" aria-label="Family standing by the open boot of a car"></div>
  <div class="review-name">The Moreira Family</div>
  <p class="review-text">Lorem Ipsum is simply dummy text of the printing and typesetting industry. Lorem Ipsum has been the industry's standard dummy text ever since the 1500s.</p>
  <div class="quote">”</div>
</article>

<!-- footer -->
<footer class="site-footer abs">
  <div class="footer-ring abs"></div>
  <div class="footer-brand abs"><div class="brand-name">MARLENIC</div><div class="brand-tag">Vehicle Rental</div></div>
  <p class="footer-about abs">Lorem Ipsum is simply dummy text of the printing and typesetting industry. Lorem Ipsum has been the industry's standard dummy text ever since the 1500s.</p>
  <span class="social abs" style="left:124px"></span>
  <span class="social abs" style="left:160px"></span>
  <span class="social abs" style="left:196px"></span>
  <span class="social abs" style="left:231px"></span>

  <h3 class="footer-heading abs" style="left:393px;top:112px">Information Links</h3>
  <ul class="footer-links abs" style="list-style:none">
    <li>Home</li><li>Fleet</li><li>Promotions</li><li>Extras &amp; Services</li><li>About Us</li><li>Partners</li><li>Contact Us</li><li>Rates &amp; Reservations</li>
  </ul>

  <h3 class="footer-heading abs" style="left:608px;top:140px">Contact Info</h3>
  <div class="contact-item abs" style="top:208px"><span class="contact-icon"><svg width="11" height="11" viewBox="0 0 24 24" fill="#fff"><path d="M7 3h4l1.5 5-2.5 2a11 11 0 0 0 5 5l2-2.5 5 1.5v4a2 2 0 0 1-2 2A17 17 0 0 1 5 5a2 2 0 0 1 2-2z"/></svg></span><span style="padding-top:3px">123-456-7890</span></div>
  <div class="contact-item abs" style="top:254px"><span class="contact-icon"><svg width="11" height="9" viewBox="0 0 12 9" fill="none" stroke="#fff" stroke-width="1.3"><rect x=".7" y=".7" width="10.6" height="7.6"/><path d="M.7 .7L6 5l5.3-4.3"/></svg></span><span style="padding-top:3px">info@marlenic.com</span></div>
  <div class="contact-item abs" style="top:301px"><span class="contact-icon"><svg width="10" height="12" viewBox="0 0 10 12" fill="#fff"><path d="M5 0a4.5 4.5 0 0 0-4.5 4.5C.5 8 5 12 5 12s4.5-4 4.5-7.5A4.5 4.5 0 0 0 5 0zm0 6.3a1.8 1.8 0 1 1 0-3.6 1.8 1.8 0 0 1 0 3.6z"/></svg></span><span>Lorem ipsum is a<br>dummy text</span></div>

  <h3 class="footer-heading abs" style="left:810px;top:198px">Subscribe to our newsletter</h3>
  <div class="news-input abs">Email Address...</div>
  <div class="news-submit abs">SUBMIT</div>
</footer>

</body>
</html>
```